Create branded design templates/backgrounds for social media based on UK property investing company

I'd like Instagram, Facebook and Linkedin backgrounds/templates to add text to, based on my logo design and business of UK holiday let investing. Ideally I'd have some base designs for me to approve, then engage with the winning designer further to create about 50 different templates. I looking for a mixture of templates with the logo and using logo colours, others of internal holiday let photos including logos and a few of my photo imposed on the front of them.
Updates

Slow in providing feedback

Target Market(s)

Middle aged adults

Industry/Entity Type

Holiday let properties

Requirements
Must have
• a distinct brand look that can be replicated

```html
<!DOCTYPE html>
<html lang="en">
<head>
<meta charset="utf-8">
<title>Holiday Home UK – Social Template</title>
<link href="https://fonts.googleapis.com/css2?family=Inter:wght@400;500;600;700&display=swap" rel="stylesheet">
<style>
  :root {
    --brand-blue: #0586cb;
    --white: #ffffff;
    --ink: #3b3b3b;
    --ink-soft: #555a5e;
    --tick-green: #58a51c;
    --divider: #b9d3a6;
    --page-bg: #eceff1;
  }
  * { box-sizing: border-box; margin: 0; padding: 0; }
  html, body {
    width: 886px; height: 1200px; overflow: hidden;
    background: var(--page-bg);
    font-family: "Inter", sans-serif;
  }
  .canvas { position: relative; width: 886px; height: 1200px; }

  .post {
    position: absolute; left: 23px; top: 181px;
    width: 724px; height: 722px;
    transform: scale(1.16); transform-origin: top left;
    background: var(--brand-blue);
    overflow: hidden;
  }

  .header-band {
    position: absolute; left: 0; top: 0; width: 724px; height: 118px;
    background: var(--brand-blue);
  }
  .headline {
    position: absolute; left: 40px; top: 30px;
    color: var(--white); font-weight: 600; font-size: 49px; letter-spacing: -0.5px;
    line-height: 1.1;
  }

  .hero-photo {
    position: absolute; left: 0; top: 118px; width: 724px; height: 280px;
    background: linear-gradient(180deg, #cfe0ea 0%, #e9ecec 35%, #d8d6d2 62%, #7aa047 78%, #5f8d34 100%);
  }

  .brand-tab { position: absolute; left: 492px; top: 0; width: 202px; height: 154px; z-index: 2; }
  .brand-name {
    position: absolute; left: 492px; top: 40px; width: 202px; z-index: 3;
    display: flex; align-items: center; justify-content: center; gap: 8px;
    color: var(--ink); font-weight: 600; font-size: 16px; white-space: nowrap;
  }
  .brand-name .brand-square { width: 14px; height: 14px; background: var(--brand-blue); flex: none; }

  .info-card {
    position: absolute; left: 12px; top: 360px; width: 700px; height: 348px;
    background: var(--white); border-radius: 10px; z-index: 4;
  }
  .agent-photo {
    position: absolute; left: 18px; top: 45px; width: 228px; height: 248px;
    background: linear-gradient(180deg, #eef0f1 0%, #e3d4ca 45%, #6f6f69 100%);
  }

  .facilities { position: absolute; left: 260px; top: 24px; width: 140px; }
  .facilities h2 {
    color: var(--brand-blue); font-weight: 600; font-size: 18px; line-height: 1.4;
  }
  .facility-list { list-style: none; margin-top: 14px; }
  .facility-list li {
    display: flex; align-items: center; gap: 8px;
    height: 28.5px; font-size: 10.5px; color: var(--ink-soft);
  }
  .facility-list svg { width: 14px; height: 14px; flex: none; }
  .call-to-invest {
    margin-top: 10px; font-size: 13px; line-height: 1.45; color: var(--ink-soft);
  }

  .gallery {
    position: absolute; left: 403px; top: 19px;
    display: grid; grid-template-columns: 134px 134px; grid-template-rows: 118px 118px;
    column-gap: 12px; row-gap: 16px;
  }
  .gallery .tile { width: 134px; height: 118px; }
  .tile-pool { background: linear-gradient(180deg, #c9d8e4 0%, #a89a7c 45%, #5fb2c9 75%, #9aa38d 100%); }
  .tile-cottage { background: linear-gradient(180deg, #dfe7ee 0%, #6e7f55 40%, #8a5e4b 60%, #55803a 100%); }
  .tile-living { background: linear-gradient(180deg, #efece7 0%, #e4ddd2 55%, #b59a7a 100%); }
  .tile-lounge { background: linear-gradient(180deg, #e9e9e8 0%, #7d7f82 40%, #d6d2cc 70%, #a37348 100%); }

  .divider {
    position: absolute; left: 18px; top: 293px; width: 664px; height: 1px;
    background: var(--divider);
  }
  .contact-button {
    position: absolute; left: 18px; top: 300px; width: 228px; height: 39px;
    background: var(--brand-blue); color: var(--white);
    font-weight: 700; font-size: 17px; letter-spacing: 0.3px;
    display: flex; align-items: center; justify-content: center;
  }
  .contact-item {
    position: absolute; top: 309px;
    display: flex; align-items: center; gap: 9px;
    font-size: 10.5px; color: var(--ink-soft); white-space: nowrap;
  }
  .contact-item svg { width: 24px; height: 24px; flex: none; }
  .contact-phone { left: 274px; }
  .contact-address { left: 436px; }
</style>
</head>
<body>
<div class="canvas">
  <article class="post">
    <header class="header-band">
      <h1 class="headline">Holiday Home UK</h1>
    </header>

    <div class="hero-photo" role="img" aria-label="Photo of a white holiday home with dormer windows, patio furniture and lawn"></div>

    <svg class="brand-tab" viewBox="0 0 202 154" aria-hidden="true">
      <polygon points="0,0 202,0 202,118 101,154 0,118" fill="#ffffff"/>
    </svg>
    <div class="brand-name"><span class="brand-square"></span>Harbourline Lets</div>

    <section class="info-card">
      <div class="agent-photo" role="img" aria-label="Portrait photo of the company founder"></div>

      <div class="facilities">
        <h2>Our Home<br>Facilities</h2>
        <ul class="facility-list">
          <li><svg viewBox="0 0 14 14"><circle cx="7" cy="7" r="7" fill="#58a51c"/><path d="M3.8 7.2l2.2 2.2 4.2-4.4" stroke="#fff" stroke-width="1.7" fill="none" stroke-linecap="round" stroke-linejoin="round"/></svg>4x bedrooms</li>
          <li><svg viewBox="0 0 14 14"><circle cx="7" cy="7" r="7" fill="#58a51c"/><path d="M3.8 7.2l2.2 2.2 4.2-4.4" stroke="#fff" stroke-width="1.7" fill="none" stroke-linecap="round" stroke-linejoin="round"/></svg>3x bathroom</li>
          <li><svg viewBox="0 0 14 14"><circle cx="7" cy="7" r="7" fill="#58a51c"/><path d="M3.8 7.2l2.2 2.2 4.2-4.4" stroke="#fff" stroke-width="1.7" fill="none" stroke-linecap="round" stroke-linejoin="round"/></svg>2x kitchen</li>
          <li><svg viewBox="0 0 14 14"><circle cx="7" cy="7" r="7" fill="#58a51c"/><path d="M3.8 7.2l2.2 2.2 4.2-4.4" stroke="#fff" stroke-width="1.7" fill="none" stroke-linecap="round" stroke-linejoin="round"/></svg>1x front garden</li>
        </ul>
        <p class="call-to-invest">What are waiting<br>for? Invest now</p>
      </div>

      <div class="gallery">
        <div class="tile tile-pool" role="img" aria-label="Photo of a stone house with a swimming pool"></div>
        <div class="tile tile-cottage" role="img" aria-label="Photo of a timber-framed cottage with a garden"></div>
        <div class="tile tile-living" role="img" aria-label="Photo of a bright living room with shelving"></div>
        <div class="tile tile-lounge" role="img" aria-label="Photo of a lounge with fireplace and coffee table"></div>
      </div>

      <div class="divider"></div>
      <div class="contact-button">CONTACT NOW!</div>

      <div class="contact-item contact-phone">
        <svg viewBox="0 0 24 24" aria-hidden="true"><circle cx="12" cy="12" r="12" fill="#0586cb"/><path d="M8.3 6.5l1.8-.3 1.1 2.7-1.3 1c.6 1.4 1.6 2.4 3 3l1-1.3 2.7 1.1-.3 1.8c-.2.8-1 1.3-1.8 1.2-3.7-.6-6.6-3.5-7.2-7.2-.1-.8.4-1.6 1-2z" fill="#fff"/></svg>
        <span>+44 1632 960 418</span>
      </div>
      <div class="contact-item contact-address">
        <svg viewBox="0 0 24 24" aria-hidden="true"><circle cx="12" cy="12" r="12" fill="#0586cb"/><path d="M12 5.5a4.3 4.3 0 0 0-4.3 4.3c0 3.2 4.3 8.2 4.3 8.2s4.3-5 4.3-8.2A4.3 4.3 0 0 0 12 5.5z" fill="#fff"/><circle cx="12" cy="9.8" r="1.6" fill="#0586cb"/></svg>
        <span>14 Harbour Row, Seaview, SV4 2LT</span>
      </div>
    </section>
  </article>
</div>
</body>
</html>
```